RTV CRAFTED

building services
decks
pergola
renovation
extensions
general building

Target Market(s)

middle to upper class

Industry/Entity Type

building

Contact Information for Business Card

my details 0427839152 pkharlow47@mailvane.net BLD574926

Font styles to use
Serif

Colors
00AB8E
00BBA5
67D7C9
C6EFE9
E9F9F6

Requirements
Must have
• logo on the front and details on the back
Nice to have
• sharp and clean lines

```html
<!DOCTYPE html>
<html lang="en">
<head>
<meta charset="UTF-8">
<title>RTV Crafted – Business Card</title>
<link href="https://fonts.googleapis.com/css2?family=Tinos:wght@400;700&display=swap" rel="stylesheet">
<style>
  :root {
    --page-bg: #8c8c8c;
    --card-dark: #0d0d0d;
    --card-light: #ffffff;
    --teal: #00ab8e;
    --teal-bright: #00bba5;
    --ink: #1f1f1f;
    --muted: #555555;
    --white: #ffffff;
  }
  * { box-sizing: border-box; margin: 0; padding: 0; }
  html, body {
    width: 900px;
    height: 1200px;
    overflow: hidden;
  }
  body {
    background: var(--page-bg);
    font-family: "Tinos", "Times New Roman", serif;
    position: relative;
  }
  .card {
    position: absolute;
    left: 120px;
    width: 660px;
    height: 372px;
    border-radius: 18px;
    overflow: hidden;
  }
  .card--front { top: 200px; background: var(--card-dark); color: var(--white); }
  .card--back  { top: 640px; background: var(--card-light); color: var(--ink); }

  .brand-name {
    font-family: "Tinos", "Times New Roman", serif;
    font-weight: 400;
    letter-spacing: 1px;
    white-space: nowrap;
  }
  .card--front .brand-name {
    position: absolute;
    top: 110px;
    width: 100%;
    text-align: center;
    font-size: 54px;
    color: var(--white);
  }
  .front-tagline {
    position: absolute;
    top: 244px;
    width: 100%;
    text-align: center;
    font-size: 19px;
    letter-spacing: 2px;
    color: var(--teal-bright);
  }
  .front-services {
    position: absolute;
    top: 278px;
    width: 100%;
    text-align: center;
    font-size: 15px;
    letter-spacing: 1px;
    color: var(--white);
  }

  .card--back .brand-name {
    position: absolute;
    top: 140px;
    left: 40px;
    font-size: 36px;
    color: var(--ink);
  }
  .divider {
    position: absolute;
    left: 318px;
    top: 100px;
    width: 2px;
    height: 150px;
    background: var(--teal);
  }
  .contact {
    position: absolute;
    left: 336px;
    top: 98px;
  }
  .contact__name {
    font-size: 30px;
    font-variant: small-caps;
    letter-spacing: 1px;
    color: var(--teal);
    line-height: 1.1;
  }
  .contact__role {
    font-size: 15px;
    color: var(--muted);
    margin-top: 6px;
    margin-bottom: 14px;
  }
  .contact__line {
    display: flex;
    align-items: center;
    gap: 10px;
    font-size: 16px;
    color: var(--ink);
    margin-bottom: 10px;
  }
  .contact__icon { width: 14px; height: 14px; flex: none; }
  .licence {
    position: absolute;
    bottom: 26px;
    width: 100%;
    text-align: center;
    font-size: 16px;
    font-weight: 700;
    letter-spacing: 1px;
    color: var(--ink);
  }
  .licence__prefix { color: var(--teal); }
</style>
</head>
<body>
  <section class="card card--front">
    <div class="brand-name">RTV CRAFTED</div>
    <div class="front-tagline">BUILDING SERVICES</div>
    <div class="front-services">DECKS | PERGOLA | RENOVATION | EXTENSIONS | GENERAL BUILDING</div>
  </section>

  <section class="card card--back">
    <div class="brand-name">RTV CRAFTED</div>
    <div class="divider"></div>
    <div class="contact">
      <div class="contact__name">Peter Harlow</div>
      <div class="contact__role">Owner</div>
      <div class="contact__line">
        <svg class="contact__icon" viewBox="0 0 24 24" aria-hidden="true">
          <path fill="#00ab8e" d="M6.6 10.8a15.1 15.1 0 0 0 6.6 6.6l2.2-2.2a1 1 0 0 1 1-.25 11.4 11.4 0 0 0 3.6.57 1 1 0 0 1 1 1V20a1 1 0 0 1-1 1A17 17 0 0 1 3 4a1 1 0 0 1 1-1h3.5a1 1 0 0 1 1 1c0 1.25.2 2.45.57 3.57a1 1 0 0 1-.25 1z"/>
        </svg>
        <span>0427839152</span>
      </div>
      <div class="contact__line">
        <svg class="contact__icon" viewBox="0 0 24 24" aria-hidden="true">
          <rect x="2" y="5" width="20" height="14" rx="1.5" fill="#00ab8e"/>
          <path d="M3 6.5l9 6 9-6" fill="none" stroke="#ffffff" stroke-width="1.8"/>
        </svg>
        <span>pkharlow47@mailvane.net</span>
      </div>
    </div>
    <div class="licence"><span class="licence__prefix">BLD</span>574926</div>
  </section>
</body>
</html>
```